Hospital Digital Whiteboard UI/UX Redesign

We are looking to update the look and feel of our Digital Whiteboards.
There are 4 separate layouts: Patient TV, Patient Room Whiteboard, Digital Door Sign, and Unit Care Board.
We want to have a unified, modern look across the portfolio.

```html
<!DOCTYPE html>
<html lang="en">
<head>
<meta charset="utf-8">
<title>Room 216 Door Sign Screens</title>
<link href="https://fonts.googleapis.com/css2?family=Montserrat:wght@400;500;600;700;800&display=swap" rel="stylesheet">
<style>
:root{
  --page:#ffffff;
  --sky-1:#d7f0fb;
  --sky-2:#bfe6f8;
  --sky-3:#7fcdf0;
  --card:#eef2fa;
  --ink:#111111;
  --room-blue:#3f6fd8;
  --cp:#de3b2e;
  --dp:#d8352c;
  --la:#ee7d1f;
  --fr:#f1b020;
  --en:#2f8a3f;
  --ns:#27a79b;
  --ve:#2c506f;
  --welcome:#6cbf4a;
  --water:#3d8fe0;
  --bed:#6a3f9f;
  --code:rgba(64,70,214,.93);
  --calm-1:#8fa3f4;
  --calm-2:#3f5ee8;
}
*{box-sizing:border-box;margin:0;padding:0}
html,body{width:1008px;height:1200px;overflow:hidden;background:var(--page)}
body{font-family:"Montserrat",sans-serif;color:var(--ink);position:relative}
.screens{position:absolute;left:24px;top:386px;display:flex;gap:30px}
.screen{position:relative;width:300px;height:428px;overflow:hidden;
  background:linear-gradient(160deg,var(--sky-2) 0%,var(--sky-1) 45%,#e6f6fd 100%)}
.screen::before{content:"";position:absolute;left:-60px;bottom:-40px;width:180px;height:300px;border-radius:50%;
  background:radial-gradient(ellipse at center,var(--sky-3) 0%,rgba(127,205,240,0) 70%);opacity:.7}
.tabs{position:absolute;left:21px;top:17px;display:flex;flex-direction:column;gap:8px}
.tab{width:43px;height:42px;border-radius:6px;color:#fff;text-align:center;padding-top:7px;box-shadow:0 2px 4px rgba(0,0,0,.18)}
.tab b{display:block;font-size:13px;font-weight:700;line-height:1.1}
.tab span{display:block;font-size:6px;font-weight:500}
.tab.cp{background:var(--cp)}.tab.dp{background:var(--dp)}.tab.la{background:var(--la)}.tab.fr{background:var(--fr)}
.tab.en{background:var(--en)}.tab.ns{background:var(--ns)}.tab.ve{background:var(--ve)}
.room{position:absolute;left:90px;top:17px;width:187px;height:77px;background:var(--card);border-radius:5px;
  text-align:center;box-shadow:0 2px 6px rgba(0,0,0,.15)}
.room small{display:block;color:var(--room-blue);font-size:12px;margin-top:10px}
.room strong{display:block;font-size:44px;font-weight:800;line-height:1;letter-spacing:-1px}
.status{position:absolute;left:90px;top:106px;width:187px;height:92px;background:var(--welcome);border-radius:3px;
  color:#fff;font-weight:800;font-size:23px;line-height:1.12;text-align:center;padding-top:20px}
.visit-label{position:absolute;left:90px;top:214px;width:187px;text-align:center;font-size:12px;font-weight:500}
.staff{position:absolute;left:90px;top:232px;width:187px;height:50px;background:#fff;border-radius:3px;display:flex;align-items:center;padding-left:11px;gap:12px}
.avatar{width:36px;height:36px;border-radius:50%;background:linear-gradient(180deg,#9ab6d2,#dfe8f1);border:1px solid #8fa1b8}
.staff .name{font-size:9.5px;font-weight:600}
.meta{font-size:6px;display:flex;gap:8px;margin-top:5px;align-items:center}
.meta span{display:flex;align-items:center;gap:2px}
.call{position:absolute;left:90px;width:187px;height:38px;border-radius:3px;padding:6px 13px;background:#fff}
.call b{display:block;font-size:13px;font-weight:700}
.call span{font-size:5.5px}
.call time{position:absolute;right:12px;bottom:9px;font-size:5.5px;display:flex;align-items:center;gap:3px}
.call.water{top:298px}.call.water b{color:var(--water)}
.call.bed{top:340px;background:var(--bed);color:#fff}
.toolbar{position:absolute;left:90px;top:387px;width:187px;height:22px;display:flex;gap:6px}
.tool{flex:1;background:#fff;border-radius:3px;display:flex;align-items:center;justify-content:center;gap:4px;font-size:5.5px;font-weight:500}
.brand{color:#6cbf4a;font-size:7px;font-weight:600;gap:3px}
.brand i{width:6px;height:6px;border-radius:50%;background:#6cbf4a;display:block}
.alert{position:absolute;left:90px;top:105px;width:187px;height:302px;background:var(--code);color:#fff;text-align:center;border-radius:2px}
.alert h2{font-size:33px;font-weight:800;line-height:1.12;margin-top:78px}
.timer{position:absolute;left:0;right:0;bottom:40px;font-size:22px;font-weight:600;line-height:1}
.timer small{display:block;font-size:16px;font-weight:500;margin-top:4px}
.screen.calm{background:linear-gradient(180deg,var(--calm-1) 0%,#7e93f2 40%,var(--calm-2) 100%)}
.screen.calm::before{display:none}
.waves{position:absolute;left:0;top:135px;width:300px;height:293px;
  background:radial-gradient(ellipse at 85% 90%,#2a47e0 0%,rgba(42,71,224,0) 60%),radial-gradient(ellipse at 20% 20%,#3552e6 0%,rgba(53,82,230,0) 55%)}
.screen.calm .room{left:35px;top:26px;width:226px;height:85px;background:#c9d2f6}
.screen.calm .room small{margin-top:12px}
.quote{position:absolute;left:26px;top:163px;width:245px;height:173px;background:#fff;border-radius:10px;text-align:center;padding-top:16px}
.quote .mark{color:var(--room-blue);font-size:22px;font-weight:800;line-height:.6}
.quote p{color:var(--room-blue);font-size:21px;line-height:1.15;margin-top:8px}
.quote cite{display:block;font-style:normal;font-size:13px;margin-top:9px}
.screen.calm .toolbar{left:21px;top:383px;width:258px;height:28px;gap:3px}
</style>
</head>
<body>
<main class="screens">

  <section class="screen">
    <nav class="tabs">
      <div class="tab cp"><b>CP</b><span>Contact</span></div>
      <div class="tab dp"><b>DP</b><span>Contact</span></div>
      <div class="tab la"><b>LA</b><span>Contact</span></div>
      <div class="tab fr"><b>FR</b><span>Contact</span></div>
      <div class="tab en"><b>EN</b><span>Contact</span></div>
      <div class="tab ns"><b>NS</b><span>Contact</span></div>
      <div class="tab ns"><b>NS</b><span>Contact</span></div>
      <div class="tab ve"><b>VE</b><span>Contact</span></div>
    </nav>
    <div class="room"><small>Room</small><strong>216</strong></div>
    <div class="status">VISITOR<br>WELCOME</div>
    <div class="visit-label">Last Staff Visit</div>
    <div class="staff">
      <div class="avatar" role="img" aria-label="Staff member portrait"></div>
      <div><div class="name">Maya Torres, R.N</div>
        <div class="meta"><span>▦ 6/01/2023</span><span>◷ 1:59 AM</span></div></div>
    </div>
    <div class="call water"><b>WATER</b><span>Nurser Call</span><time>◷ 1:59 AM</time></div>
    <div class="call bed"><b>BED HEIGHT</b><span>Nurser Call</span><time>◷ 1:59 AM</time></div>
    <div class="toolbar">
      <div class="tool"><svg width="7" height="8" viewBox="0 0 7 8"><path d="M3.5 0a2.6 2.6 0 0 0-2.6 2.6C.9 4.6 3.5 7.5 3.5 7.5s2.6-2.9 2.6-4.9A2.6 2.6 0 0 0 3.5 0z" fill="#3aa04a"/></svg>Floor Map</div>
      <div class="tool brand"><i></i>Clearwell</div>
      <div class="tool"><svg width="8" height="8" viewBox="0 0 8 8"><circle cx="4" cy="4" r="3" fill="none" stroke="#3d8fe0" stroke-width="1.6"/></svg>Admin</div>
    </div>
  </section>

  <section class="screen">
    <nav class="tabs">
      <div class="tab cp"><b>CP</b><span>Contact</span></div>
      <div class="tab dp"><b>DP</b><span>Contact</span></div>
      <div class="tab la"><b>LA</b><span>Contact</span></div>
      <div class="tab fr"><b>FR</b><span>Contact</span></div>
      <div class="tab en"><b>EN</b><span>Contact</span></div>
      <div class="tab ns"><b>NS</b><span>Contact</span></div>
      <div class="tab ns"><b>NS</b><span>Contact</span></div>
      <div class="tab ve"><b>VE</b><span>Contact</span></div>
    </nav>
    <div class="room"><small>Room</small><strong>216</strong></div>
    <div class="status">VISITOR<br>WELCOME</div>
    <div class="visit-label">Last Staff Visit</div>
    <div class="staff">
      <div class="avatar" role="img" aria-label="Staff member portrait"></div>
      <div><div class="name">Maya Torres, R.N</div>
        <div class="meta"><span>▦ 6/01/2023</span><span>◷ 1:59 AM</span></div></div>
    </div>
    <div class="call water"><b>WATER</b><span>Nurser Call</span><time>◷ 1:59 AM</time></div>
    <div class="call bed"><b>BED HEIGHT</b><span>Nurser Call</span><time>◷ 1:59 AM</time></div>
    <div class="alert">
      <h2>CODE<br>BLUE</h2>
      <div class="timer">⧖02:24<small>Elapse Time</small></div>
    </div>
  </section>

  <section class="screen calm">
    <div class="waves" role="img" aria-label="Soft blue flowing wave background"></div>
    <div class="room"><small>Room</small><strong>216</strong></div>
    <blockquote class="quote">
      <div class="mark">❞</div>
      <p>“Believe you<br>can and you’re<br>halfway there.”</p>
      <cite>— Eleanor Whitby</cite>
    </blockquote>
    <div class="toolbar">
      <div class="tool"><svg width="7" height="8" viewBox="0 0 7 8"><path d="M3.5 0a2.6 2.6 0 0 0-2.6 2.6C.9 4.6 3.5 7.5 3.5 7.5s2.6-2.9 2.6-4.9A2.6 2.6 0 0 0 3.5 0z" fill="#3aa04a"/></svg>Floor Map</div>
      <div class="tool brand"><i></i>Clearwell</div>
      <div class="tool"><svg width="9" height="9" viewBox="0 0 8 8"><circle cx="4" cy="4" r="3" fill="none" stroke="#3d8fe0" stroke-width="1.6"/></svg>Admin</div>
    </div>
  </section>

</main>
</body>
</html>
```